Business Cards for Communications Technology Company

We are an innovative software company based in Tropical North Queensland, Australia. We have several brands with a focus on communications software for businesses. We are looking for a business card that is very innovate and creative whilst still remaining professional on a corporate level.

Our internal culture is very progressive and expresses a blend between the clarity of our natural surroundings and the highly technological industry we work in. Our current branding blends a modern minimalist typeface with the desire to push the boundaries in the way we communicate.

This is a corporate level business card for the communications software industry and may possibly also encompass our brands MarNetwork, PelFax, TukMailer and our B2B marketing service—with our companies name being Viresca Partners. Showing other brands on the business card is optional not compulsory.

Technical notes:

-We will attach all logo's and some examples of our corporate branding
- Would be willing to print with various papers, embossed, metallic ink, curved edges etc. in a standard business card size

Sample content:

Rowan Pellick
Senior Account Manager
Phone: 1300 842 916 / +617 4583 2764
Email: r.pellick@viresca.com.au
Web: www.viresca.com.au

Sincerely,
Viresca Partners.

```html
<!DOCTYPE html>
<html lang="en">
<head>
<meta charset="utf-8">
<title>Viresca Partners — Business Cards</title>
<link href="https://fonts.googleapis.com/css2?family=Lato:wght@300;400;700&display=swap" rel="stylesheet">
<style>
  :root {
    --backdrop: #141617;
    --card: #212528;
    --card-edge: #2b3034;
    --ink-light: #f2f2f2;
    --ink-soft: #c9cccf;
    --ink-muted: #8d9296;
    --green: #7dc142;
    --blue: #3d6fb6;
    --orange: #f06a22;
  }
  * { box-sizing: border-box; margin: 0; padding: 0; }
  html, body {
    width: 1200px; height: 1076px; overflow: hidden;
    background: var(--backdrop);
    font-family: "Lato", sans-serif;
  }
  .stage {
    position: relative; width: 1200px; height: 1076px;
  }
  .card {
    position: absolute; left: 210px; width: 780px; height: 460px;
    background: var(--card);
    border: 1px solid var(--card-edge);
    border-radius: 6px;
    box-shadow: 0 14px 40px rgba(0,0,0,.55);
    overflow: hidden;
  }
  .card--front { top: 58px; }
  .card--back { top: 558px; }

  /* front */
  .brand-lockup {
    position: absolute; left: 0; right: 0; top: 150px;
    display: flex; align-items: center; justify-content: center; gap: 22px;
  }
  .brand-mark {
    width: 64px; height: 64px; border-radius: 50%;
    background: #0e1011;
  }
  .brand-name {
    font-weight: 300; font-size: 58px; letter-spacing: 1px;
    color: var(--ink-soft);
  }
  .product-row {
    position: absolute; left: 0; right: 0; top: 330px;
    display: flex; justify-content: center; align-items: center; gap: 28px;
    font-weight: 700; font-size: 27px;
  }
  .product--mailer { color: var(--blue); }
  .product--fax { color: var(--green); }
  .product--network { color: var(--orange); }
  .product-divider { color: var(--ink-soft); font-weight: 300; font-size: 32px; }

  /* back */
  .card--back .brand-lockup {
    left: 48px; right: auto; top: 48px; justify-content: flex-start; gap: 18px;
  }
  .card--back .brand-mark { width: 58px; height: 58px; background: var(--green); }
  .card--back .brand-name { font-size: 50px; color: var(--ink-light); }

  .holder { position: absolute; left: 58px; top: 208px; }
  .holder-name {
    font-weight: 700; font-size: 34px; color: var(--ink-light); letter-spacing: .5px;
  }
  .holder-role {
    font-weight: 400; font-size: 26px; color: var(--green); margin-top: 2px;
  }
  .contact { position: absolute; left: 58px; top: 320px; }
  .contact-line {
    display: flex; align-items: center; gap: 14px;
    font-size: 25px; color: var(--ink-light); line-height: 38px;
  }
  .contact-icon { width: 26px; height: 26px; flex: none; }
  .contact-web { padding-left: 0; margin-top: 4px; }
  .contact-web .accent { color: var(--green); }
</style>
</head>
<body>
<main class="stage">

  <section class="card card--front" aria-label="Card front">
    <div class="brand-lockup">
      <span class="brand-mark"></span>
      <span class="brand-name">Viresca Partners</span>
    </div>
    <div class="product-row">
      <span class="product product--mailer">TukMailer</span>
      <span class="product-divider">/</span>
      <span class="product product--fax">PelFax</span>
      <span class="product-divider">/</span>
      <span class="product product--network">MarNetwork</span>
    </div>
  </section>

  <section class="card card--back" aria-label="Card back">
    <div class="brand-lockup">
      <span class="brand-mark"></span>
      <span class="brand-name">Viresca Partners</span>
    </div>

    <div class="holder">
      <p class="holder-name">Rowan Pellick</p>
      <p class="holder-role">Senior Account Manager</p>
    </div>

    <div class="contact">
      <p class="contact-line">
        <svg class="contact-icon" viewBox="0 0 26 26" aria-hidden="true">
          <circle cx="13" cy="13" r="11.5" fill="none" stroke="#7dc142" stroke-width="2"/>
          <path d="M8 9.5c0-1 .8-1.6 1.6-1.6h1.2l1.2 3-1.4 1c.7 1.5 1.8 2.6 3.3 3.3l1-1.4 3 1.2v1.2c0 .8-.6 1.6-1.6 1.6C11.6 17.8 8 14.3 8 9.5z" fill="#7dc142"/>
        </svg>
        1300 842 916 / +617 4583 2764
      </p>
      <p class="contact-line">
        <svg class="contact-icon" viewBox="0 0 26 26" aria-hidden="true">
          <circle cx="13" cy="13" r="11.5" fill="none" stroke="#7dc142" stroke-width="2"/>
          <rect x="7" y="9" width="12" height="8.5" rx="1" fill="#7dc142"/>
          <path d="M7.5 9.5 13 14l5.5-4.5" fill="none" stroke="#212528" stroke-width="1.3"/>
        </svg>
        r.pellick@viresca.com.au
      </p>
      <p class="contact-line contact-web">www.<span class="accent">viresca</span>.com.au</p>
    </div>
  </section>

</main>
</body>
</html>
```